Beekeeper needs a label for honey jars

Ciao! I'm from Como Italy
I'm a hobbyist beekeeper and I produce honey for myself and my friends.
I've named my apiary "Dado di sole," a play on words between my nickname (Dado, from Edoardo) and the Italian expression "Dado di sole," which translates to "a drizzle of honey" in English.
I need to create a label for my honey glass jars (250 gr and 500 gr).
I don't need a label for commercial purposes. I would like to include at least the name “Apicoltura Dado di sole", the type of honey (e.g., wildflower, acacia...) and a space for the production year, to be handwritten each year.
In the design some references to the world of bees.
For reference, attached a label with a style I like
Attached are the images of the selected jars and their measurements
Thanks and good job!

beekeeping, honey

• I would like an elegant style with clean graphics.
• Predominance of black color.

```html
<!DOCTYPE html>
<html lang="en">
<head>
<meta charset="UTF-8">
<title>Apicoltura Dado di sole – Honey Jar Label</title>
<link rel="stylesheet" href="https://fonts.googleapis.com/css2?family=Roboto:wght@400;500;700&display=swap">
<style>
  :root {
    --stage-bg: #ece9e2;
    --label-black: #141414;
    --label-black-edge: #2a2a2a;
    --honey-gold: #dcb232;
    --ink-light: #f2f2f2;
    --on-gold: #141414;
    --art-light: #3a3220;
    --art-deep: #8a7024;
  }
  html, body {
    margin: 0;
    padding: 0;
    width: 1200px;
    height: 803px;
    overflow: hidden;
    background: var(--stage-bg);
    font-family: "Roboto", Arial, sans-serif;
  }
  .stage {
    position: relative;
    width: 1200px;
    height: 803px;
  }
  .jar-label {
    position: absolute;
    left: 270px;
    top: 101px;
    width: 660px;
    height: 600px;
    box-shadow: 0 10px 30px rgba(0,0,0,0.18);
  }
  .brand-arc { fill: var(--honey-gold); font-weight: 700; font-size: 31px; letter-spacing: 1px; }
  .product-name { fill: var(--honey-gold); font-weight: 700; font-size: 66px; }
  .natural-note { fill: var(--honey-gold); font-weight: 500; font-size: 13px; letter-spacing: 2px; }
  .year-label { fill: var(--ink-light); font-weight: 400; font-size: 15px; }
  .year-line { stroke: var(--honey-gold); stroke-width: 1; }
  .volume { fill: var(--ink-light); font-weight: 400; font-size: 17px; }
  .claim-box { fill: var(--honey-gold); }
  .claim-text { fill: var(--on-gold); font-weight: 400; font-size: 17px; }
</style>
</head>
<body>
<main class="stage">
  <svg class="jar-label" viewBox="0 0 440 400" xmlns="http://www.w3.org/2000/svg" aria-label="Apicoltura Dado di sole honey label">
    <defs>
      <linearGradient id="label-paper" x1="0" y1="0" x2="1" y2="0">
        <stop offset="0" stop-color="var(--label-black)"/>
        <stop offset="0.6" stop-color="var(--label-black)"/>
        <stop offset="1" stop-color="var(--label-black-edge)"/>
      </linearGradient>
      <radialGradient id="bee-art-fill" cx="0.5" cy="0.5" r="0.55">
        <stop offset="0" stop-color="var(--art-deep)"/>
        <stop offset="1" stop-color="var(--art-light)"/>
      </radialGradient>
      <path id="brand-curve" d="M 22 108 Q 220 -22 418 108"/>
    </defs>

    <rect class="label-paper" x="0" y="0" width="440" height="400" fill="url(#label-paper)"/>

    <text class="brand-arc" text-anchor="middle">
      <textPath href="#brand-curve" startOffset="50%">APICOLTURA DADO DI SOLE</textPath>
    </text>

    <ellipse class="bee-art" role="img" aria-label="Line illustration of a honey bee with spread wings"
             cx="220" cy="128" rx="80" ry="50" fill="url(#bee-art-fill)" opacity="0.7"/>

    <text class="product-name" x="220" y="242" text-anchor="middle">Honey</text>
    <text class="natural-note" x="220" y="266" text-anchor="middle">100% NATURAL</text>

    <text class="year-label" x="140" y="308">Year</text>
    <line class="year-line" x1="178" y1="308" x2="300" y2="308"/>

    <text class="volume" x="220" y="345" text-anchor="middle">250 ML &#160;| 8.5 OZ</text>

    <rect class="claim-box" x="47" y="362" width="168" height="26"/>
    <text class="claim-text" x="131" y="381" text-anchor="middle">No Preservatives</text>
    <rect class="claim-box" x="222" y="362" width="168" height="26"/>
    <text class="claim-text" x="306" y="381" text-anchor="middle">Wildflower Honey</text>
  </svg>
</main>
</body>
</html>
```